Brennick Setter Club - Rare dog breed club needs web design!

The Transylvanian Hound (or Erdélyi kopó) is an ancient Hungarian dog breed. These medium-sized hounds were favored by the Hungarian kings and princes for hunting bears and wolves in the Carpathian mountains of Transylvania. The breed's great adaptability to the region's extreme climates of sweltering summers and frigid winters made it an excellent all season hunting dog. This dog has a sleek appearance and stunning good looks. They are lean, appear very elegant and proud. Their erect posture and beautifully sculpted head portray great attentiveness and authority. In general, this rare breed is extremely good natured, loyal and obedient. It has a tendency to form strong attachments to its primary caretakers and will remain loyal and protective. (Please refer to existing web resources.)

The Brennick Setter Club - with current website www.brennicksetter.com - is the official breed club of Transylvanian Hound afficionados, breeders and owners in the United States, which was founded in 2010. We are looking for a web design for the new, upgraded version of this central (currenty non-functioning) website. Please do not recycle the old logo (we may choose from your suggesions and pay for it!) or any of the old texts. Please use the structure described below. Overall, the webpage serves a dual purpose: an educational one (about the breed itself) and a community-building one (inside the Club). The proposed structure of the website is as follows:

1. About the Kopó
- Breed History
- Breed Standard
- Public Education
- Photo Gallery

2. Life with a Kopó
- Health and Genetics
- Feeding and Nutrition
- Training and Activities

3. Finding a Kopó
- Is this the Right Breed for You?
- Choosing a Puppy
- FAQ
- Breeder Referral

4. The Brennick Setter Club
- Constituton
- Officers and Appointees
- Code of Ethics
- Breeder Guidelines
- Membership
- Reports
- Links

5. News and Events

6. Shop

We are attaching a couple of examples of the graphics/drawings of the dogs that would be part of the design of the website. We plan to have more of these artistic depictions, nicely embedded into the background (maybe shaded out at the edges just like the drawings themselves) and less actual photos. Or a good combination of the two.

Further information upon request.

Reason: There are a few very promising design collaborations ongoing. As we moved the brief to a more artistic and graphic direction, we felt that one week of extension would be needed to get to the perfect end-product, which could include designs for sub-pages as well.

Reason: In order to make the final modifications to the leading designs, and at the request of those designers, the deadline is extended until Friday.

Target Market(s)

- BRSC Club members, dog (especially T-Hound) owners, past and future owners, breeders, puppy buyers, hunters, kennel clubs, dog show participants, vets, animal shelters, Hungarian, Romanian and other European web visitors, historians

Industry/Entity Type

Club

Font styles to use
Serif
Decorative
Script

Requirements
Must have
• - Sync with graphics of dogs (see attachments), but accentuate the rich black basic color of the dogs
- Elegance, aristocratic/noble look and feel (but not overly archaic)
- Love, companionship, dogs as family members
- Hunting usage, but no bloody associations, rather romantic ones
- Simple to use and navigate for non-web-natives
- Old world (Central European) atmosphere, even the exotic, rustic and romantic Transylvanian feel - SEE the new attachment for inspiration (this was a design plan which we discarded (mainly because of its gothic, (nazi-like), unreadable font, and the fact that the plan makes the black-looking dogs appear brown), however we loved the fact that it was not full of boxes/windows, had a marble/sand stone like continuous background, lots of little elegant graphics, the drawings embedded, etc.
Nice to have
• - Working on smartphone, Zentabs, etc., so dynamic website design
- Web shop to be added to functionalities in the future (?)
- English language for now, in the future can be Hungarian, Romanian, etc., so the font choice should handle various alphabets
- Focus on the dogs (likely more graphics than photos, at least on the main pages), and not on the activities/humans - the design should accentuate the black and not the tan of the graphics!
Should not have
• - Old logo from the old www.brennicksetter.com webpage or the other logo from the Chatterly site of the Brennick Setter Club, we will have a new one (maybe designed by you!)
- Breed club, kennel club cliches
- Cutesy, adorable, cheesy design elements
- Old, stale, monolithic, archaic, snobbish, etc. look and feel
- No vampire associations

```html
<!DOCTYPE html>
<html lang="en">
<head>
<meta charset="utf-8">
<title>Brennick Setter Club – Website Screens</title>
<link href="https://fonts.googleapis.com/css2?family=Cormorant+Garamond:wght@500&family=Oswald:wght@400&family=Raleway:wght@300;400;500&display=swap" rel="stylesheet">
<style>
  :root {
    --stage: #f3f3f3;
    --ink: #231f20;
    --ink-deep: #1a1718;
    --paper: #ffffff;
    --mist: #e6e6e6;
    --rule: #d9d9d9;
    --muted: #8a8a8a;
    --soft: #bdbdbd;
    --accent: #e0554a;
    --caption: #6d6d6d;
  }
  * { box-sizing: border-box; margin: 0; padding: 0; }
  html, body { width: 1200px; height: 496px; overflow: hidden; }
  body {
    background: var(--stage);
    font-family: "Raleway", sans-serif;
    color: var(--ink);
    position: relative;
  }

  .screen {
    position: absolute;
    background: var(--paper);
    overflow: hidden;
    display: flex;
    box-shadow: 0 0 0 1px var(--rule);
  }
  .screen--news { left: 12px; top: 107px; width: 330px; height: 206px; }
  .screen--home { left: 360px; top: 60px; width: 480px; height: 300px; }
  .screen--about { left: 858px; top: 107px; width: 330px; height: 206px; }

  /* Sidebar */
  .sidebar {
    flex: 0 0 auto;
    background: var(--paper);
    border-right: 1px solid var(--rule);
    display: flex;
    flex-direction: column;
  }
  .screen--home .sidebar { width: 62px; }
  .screen--news .sidebar, .screen--about .sidebar { width: 48px; }
  .brand {
    text-align: center;
    padding: 10px 2px 8px;
    border-bottom: 1px solid var(--rule);
    font-family: "Cormorant Garamond", serif;
    font-weight: 500;
    color: var(--ink);
    line-height: 1.05;
  }
  .screen--home .brand { font-size: 9px; padding-top: 12px; height: 78px; }
  .screen--news .brand, .screen--about .brand { font-size: 6.5px; height: 54px; }
  .brand__est { display: block; margin-top: 4px; font-size: 0.75em; }
  .nav { list-style: none; }
  .nav__item {
    font-size: 4px;
    letter-spacing: 0.12em;
    text-transform: uppercase;
    color: var(--muted);
    border-bottom: 1px solid var(--rule);
    padding-left: 8px;
    display: flex;
    align-items: center;
  }
  .screen--home .nav__item { height: 21px; font-size: 4.4px; }
  .screen--news .nav__item, .screen--about .nav__item { height: 16px; font-size: 3.6px; padding-left: 5px; }
  .nav__item--active { background: var(--ink); color: var(--paper); }

  .main { flex: 1; position: relative; overflow: hidden; }

  /* Home */
  .intro {
    text-align: center;
    font-size: 5px;
    line-height: 1.5;
    color: var(--muted);
    padding: 9px 120px 0;
  }
  .features {
    display: flex;
    justify-content: center;
    gap: 18px;
    margin-top: 8px;
  }
  .feature { width: 54px; text-align: center; }
  .feature__card {
    position: relative;
    background: var(--ink);
    color: var(--paper);
    height: 60px;
    padding: 7px 4px 0;
  }
  .feature__card::after {
    content: "";
    position: absolute;
    left: 50%;
    bottom: -5px;
    margin-left: -5px;
    border: 5px solid transparent;
    border-bottom: 0;
    border-top-color: var(--ink);
  }
  .feature__title { font-size: 5.4px; }
  .feature__sub { font-size: 2.6px; letter-spacing: 0.1em; text-transform: uppercase; color: var(--soft); margin-top: 1px; }
  .feature__text { font-size: 3px; line-height: 1.5; color: var(--soft); margin-top: 9px; }
  .feature__more { font-size: 2.8px; letter-spacing: 0.1em; text-transform: uppercase; color: var(--muted); margin-top: 12px; }

  .join {
    position: absolute;
    left: 0; right: 0; top: 112px; bottom: 0;
    background: var(--mist);
    border-top: 1px solid var(--rule);
  }
  .join__title {
    text-align: center;
    font-size: 5px;
    letter-spacing: 0.3em;
    text-transform: uppercase;
    color: var(--muted);
    margin-top: 13px;
  }
  .join__rule { width: 40px; height: 1px; background: var(--soft); margin: 4px auto 0; }
  .join__lead { text-align: center; font-size: 4.3px; color: var(--muted); margin-top: 7px; }
  .form { position: absolute; left: 176px; top: 56px; width: 60px; }
  .form__field {
    height: 5.5px;
    border: 1px solid var(--rule);
    background: var(--mist);
    font-size: 2.8px;
    color: var(--soft);
    padding-left: 2px;
    line-height: 3.5px;
    margin-bottom: 10px;
  }
  .form__field--filled { background: var(--paper); border-color: var(--soft); color: var(--ink); }
  .form__field--message { height: 26px; }
  .art {
    position: absolute;
    left: 240px; top: 50px;
    width: 64px; height: 66px;
    background: radial-gradient(ellipse at 50% 45%, #6b5a51 0%, #a89a91 45%, rgba(230,230,230,0) 72%);
  }
  .art__caption { position: absolute; left: 236px; top: 122px; font-size: 2.8px; color: var(--muted); }

  /* News */
  .news-head { background: var(--ink); height: 58px; position: relative; }
  .news-head__label {
    position: absolute; left: 78px; top: 8px;
    background: var(--paper);
    font-family: "Oswald", sans-serif;
    font-size: 7px;
    padding: 2px 8px;
    color: var(--ink);
  }
  .news-head__search {
    position: absolute; left: 70px; top: 25px;
    width: 86px; height: 6px;
    background: var(--paper);
    font-size: 2.6px; color: var(--soft);
    padding-left: 3px; line-height: 6px;
  }
  .news-head__meta { position: absolute; right: 14px; bottom: 3px; font-size: 2.6px; color: var(--soft); }
  .post { background: var(--paper); height: 62px; position: relative; }
  .post__photo {
    position: absolute; left: 48px; top: 6px;
    width: 38px; height: 30px;
    background: linear-gradient(160deg, #a7b38a, #6f7a55);
  }
  .post__title { position: absolute; left: 92px; top: 7px; font-family: "Oswald", sans-serif; font-size: 6.2px; }
  .post__date { position: absolute; left: 92px; top: 17px; font-size: 3px; color: var(--muted); }
  .post__text { position: absolute; left: 92px; top: 22px; width: 138px; font-size: 2.6px; line-height: 1.5; color: var(--muted); }
  .post__wide { position: absolute; left: 48px; top: 40px; width: 182px; font-size: 2.6px; line-height: 1.5; color: var(--muted); }
  .band { background: var(--ink-deep); height: 10px; position: relative; }
  .band__icon { position: absolute; right: 8px; top: 3px; }

  /* About */
  .about-head { background: var(--paper); height: 20px; text-align: center; border-bottom: 1px solid var(--rule); }
  .about-head__title { font-family: "Cormorant Garamond", serif; font-size: 5px; color: var(--muted); padding-top: 8px; }
  .about-body { background: var(--ink); height: 186px; padding: 14px 0 0; }
  .sections { display: grid; grid-template-columns: 64px 64px; column-gap: 26px; row-gap: 12px; justify-content: center; }
  .section { text-align: center; color: var(--paper); }
  .section__title { font-family: "Oswald", sans-serif; font-size: 4.2px; letter-spacing: 0.12em; text-transform: uppercase; line-height: 1.25; }
  .section__rule { width: 14px; height: 1px; background: var(--muted); margin: 3px auto; }
  .section__text { font-size: 2.4px; line-height: 1.5; color: var(--soft); }

  .live-note {
    position: absolute;
    left: 0; right: 0; top: 452px;
    text-align: center;
    font-family: "Raleway", sans-serif;
    font-weight: 300;
    font-size: 20px;
    letter-spacing: 0.04em;
    color: var(--caption);
  }
  .live-note__site { color: var(--accent); }
</style>
</head>
<body>

<!-- News & Events page -->
<section class="screen screen--news">
  <aside class="sidebar">
    <div class="brand">Brennick Setter Club<span class="brand__est">Est. 2010</span></div>
    <ul class="nav">
      <li class="nav__item">About the Club</li>
      <li class="nav__item">Resources</li>
      <li class="nav__item">Shop</li>
      <li class="nav__item nav__item--active">News &amp; Events</li>
      <li class="nav__item">Contact Us</li>
    </ul>
  </aside>
  <div class="main">
    <header class="news-head">
      <div class="news-head__label">News &amp; Events</div>
      <div class="news-head__search">Search the news</div>
      <div class="news-head__meta">Latest first</div>
    </header>
    <article class="post">
      <div class="post__photo" role="img" aria-label="Photo of a black and tan hound standing in a grassy field"></div>
      <h3 class="post__title">Morbi tristique elementum</h3>
      <p class="post__date">07/05/2014</p>
      <p class="post__text">Members gathered for a spring walk through the hills, with young hounds meeting the pack for the first time.</p>
      <p class="post__wide">Our next meeting takes place in early summer. All owners, breeders and friends of the breed are warmly invited to join us.</p>
    </article>
    <div class="band">
      <svg class="band__icon" width="6" height="4" viewBox="0 0 6 4"><path d="M0.5 3.5 L3 1 L5.5 3.5" fill="none" stroke="#bdbdbd" stroke-width="0.8"/></svg>
    </div>
    <article class="post">
      <div class="post__photo" role="img" aria-label="Photo of a hound resting under trees"></div>
      <h3 class="post__title">Pellentesque eu sagittis</h3>
      <p class="post__date">21/04/2014</p>
    </article>
  </div>
</section>

<!-- Home page -->
<section class="screen screen--home">
  <aside class="sidebar">
    <div class="brand">Brennick Setter Club<span class="brand__est">Est. 2010</span></div>
    <ul class="nav">
      <li class="nav__item">About the Club</li>
      <li class="nav__item">Resources</li>
      <li class="nav__item">Shop</li>
      <li class="nav__item">News &amp; Events</li>
      <li class="nav__item">Contact Us</li>
    </ul>
  </aside>
  <div class="main">
    <p class="intro">Below are some of our informative articles on Transylvanian Hound breeding, maintenance and care.</p>
    <div class="features">
      <div class="feature">
        <div class="feature__card">
          <div class="feature__title">About the Kopó</div>
          <div class="feature__sub">Breed history</div>
          <p class="feature__text">An ancient hunter of the mountain forests, noble and calm.</p>
        </div>
        <div class="feature__more">Read more</div>
      </div>
      <div class="feature">
        <div class="feature__card">
          <div class="feature__title">Life with a Kopó</div>
          <div class="feature__sub">Health &amp; genetics</div>
          <p class="feature__text">Caring for a loyal companion through every season of life.</p>
        </div>
        <div class="feature__more">Read more</div>
      </div>
      <div class="feature">
        <div class="feature__card">
          <div class="feature__title">Finding a Kopó</div>
          <div class="feature__sub">Choosing a puppy</div>
          <p class="feature__text">Is this the right breed for you? Meet our trusted breeders.</p>
        </div>
        <div class="feature__more">Read more</div>
      </div>
    </div>

    <div class="join">
      <h2 class="join__title">Become a Member</h2>
      <div class="join__rule"></div>
      <p class="join__lead">Thank you for visiting us, and please be a member of our Club.</p>
      <div class="form">
        <div class="form__field form__field--filled">Full Name</div>
        <div class="form__field">Phone Number</div>
        <div class="form__field">Email</div>
        <div class="form__field">Pay Online</div>
        <div class="form__field form__field--message">Message</div>
      </div>
      <div class="art" role="img" aria-label="Soft ink drawing of a hound's head fading into the background"></div>
      <p class="art__caption">The Kopó, a faithful friend at home.</p>
    </div>
  </div>
</section>

<!-- About the Club page -->
<section class="screen screen--about">
  <aside class="sidebar">
    <div class="brand">Brennick Setter Club<span class="brand__est">Est. 2010</span></div>
    <ul class="nav">
      <li class="nav__item nav__item--active">About the Club</li>
      <li class="nav__item">Resources</li>
      <li class="nav__item">Shop</li>
      <li class="nav__item">News &amp; Events</li>
      <li class="nav__item">Contact Us</li>
    </ul>
  </aside>
  <div class="main">
    <header class="about-head"><h2 class="about-head__title">About the Brennick Setter Club</h2></header>
    <div class="about-body">
      <div class="sections">
        <div class="section"><div class="section__title">Constitution</div><div class="section__rule"></div><p class="section__text">The founding rules that guide our club.</p></div>
        <div class="section"><div class="section__title">Officers &amp;<br>Appointees</div><div class="section__rule"></div><p class="section__text">Meet the people who lead our club.</p></div>
        <div class="section"><div class="section__title">Code of<br>Ethics</div><div class="section__rule"></div><p class="section__text">Our promise to every hound and owner.</p></div>
        <div class="section"><div class="section__title">Breeder<br>Guidelines</div><div class="section__rule"></div><p class="section__text">Standards for responsible and caring breeding.</p></div>
        <div class="section"><div class="section__title">Membership</div><div class="section__rule"></div><p class="section__text">How to join and support our club.</p></div>
        <div class="section"><div class="section__title">Reports</div><div class="section__rule"></div><p class="section__text">Yearly notes from meetings and shows.</p></div>
        <div class="section"><div class="section__title">Links</div><div class="section__rule"></div></div>
      </div>
    </div>
  </div>
</section>

<p class="live-note">Please view this website live at <span class="live-note__site">BrennickSetter</span>.sitehaven.com</p>

</body>
</html>
```